Billboard Design for Equipment Rental Business

We need a billboard design for our equipment rental business called Brindlewood Equipment Company. We are based in Georgia. We rent construction tools, equipment, and dumpsters. We currently have a design but feel like we could get something better. Our phone number is 912-730-2591 and our website is www.brindlewoodequipment-example.com

```html
<!DOCTYPE html>
<html lang="en">
<head>
<meta charset="utf-8">
<title>Brindlewood Equipment Company – Billboard</title>
<link href="https://fonts.googleapis.com/css2?family=Archivo:wdth,wght@125,900&family=Oswald:wght@700&display=swap" rel="stylesheet">
<style>
  :root{
    --yellow:#f9bd1c;
    --yellow-deep:#e9a316;
    --yellow-light:#ffd659;
    --steel:#b9b9b9;
    --ink:#1e1e1e;
    --white:#ffffff;
    --stage:#6d6d6d;
  }
  html,body{margin:0;padding:0;overflow:hidden;}
  body{width:1200px;height:1112px;background:var(--stage);position:relative;}
  .billboard{
    position:absolute;left:30px;top:348px;width:1140px;height:416px;
    background:var(--yellow);overflow:hidden;
    font-family:"Archivo",Arial,sans-serif;font-stretch:125%;font-weight:900;
  }
  .brand-mark{position:absolute;left:82px;top:10px;width:130px;height:130px;
    background:var(--yellow-deep);}
  .brand{position:absolute;left:252px;top:20px;color:var(--ink);
    font-family:"Oswald","Arial Narrow",sans-serif;font-weight:700;line-height:1;}
  .brand-name{font-size:66px;letter-spacing:1px;display:block;}
  .brand-sub{font-size:26px;letter-spacing:5px;display:block;margin-top:8px;}
  .rent-band{position:absolute;left:0;top:157px;width:413px;height:58px;}
  .rent-title{position:absolute;left:30px;top:157px;height:58px;line-height:60px;
    font-size:54px;color:var(--yellow);letter-spacing:5px;}
  .rent-list{position:absolute;left:0;top:220px;margin:0;padding:0;list-style:none;}
  .rent-list li{display:flex;align-items:center;height:41px;font-size:42px;
    color:var(--ink);letter-spacing:4px;line-height:1;white-space:nowrap;}
  .rent-list svg{width:18px;height:24px;margin-right:10px;flex:none;}
  .contact-bar{position:absolute;left:0;bottom:0;width:1140px;height:63px;}
  .phone{position:absolute;left:26px;bottom:0;height:63px;display:flex;align-items:center;
    color:var(--white);font-size:50px;letter-spacing:7px;}
  .phone svg{width:26px;height:26px;margin-right:8px;}
  .web{position:absolute;left:578px;bottom:0;height:63px;display:flex;align-items:center;
    color:var(--ink);font-size:21px;white-space:nowrap;}
  .web svg{width:22px;height:22px;margin-right:6px;}
  .tools-art{position:absolute;left:676px;top:10px;width:458px;height:356px;
    border-radius:28px;
    background:
      radial-gradient(ellipse 42% 48% at 52% 72%,var(--yellow-light) 0%,#f6b21c 70%,rgba(246,178,28,0) 72%),
      linear-gradient(160deg,#8c8c8c 0%,var(--steel) 30%,var(--yellow-deep) 60%,#d98f12 100%);}
</style>
</head>
<body>
  <div class="billboard">
    <div class="brand-mark" role="img" aria-label="Company logo mark"></div>
    <div class="brand">
      <span class="brand-name">BRINDLEWOOD</span>
      <span class="brand-sub">EQUIPMENT COMPANY</span>
    </div>

    <svg class="rent-band" viewBox="0 0 413 58" aria-hidden="true">
      <polygon points="0,0 368,0 413,58 0,58" fill="var(--ink)"/>
    </svg>
    <div class="rent-title">WE RENT</div>

    <ul class="rent-list">
      <li><svg viewBox="0 0 18 24" aria-hidden="true"><polygon points="0,0 10,0 18,12 10,24 0,24" fill="var(--ink)"/></svg>CONSTRUCTION TOOLS</li>
      <li><svg viewBox="0 0 18 24" aria-hidden="true"><polygon points="0,0 10,0 18,12 10,24 0,24" fill="var(--ink)"/></svg>EQUIPMENT AND</li>
      <li><svg viewBox="0 0 18 24" aria-hidden="true"><polygon points="0,0 10,0 18,12 10,24 0,24" fill="var(--ink)"/></svg>DUMPSTERS</li>
    </ul>

    <svg class="contact-bar" viewBox="0 0 1140 63" aria-hidden="true">
      <rect x="0" y="0" width="1140" height="63" fill="var(--white)"/>
      <polygon points="0,0 537,0 582,63 0,63" fill="var(--yellow)"/>
      <polygon points="0,0 522,0 570,63 0,63" fill="var(--ink)"/>
    </svg>

    <div class="tools-art" role="img" aria-label="Yellow hard hat surrounded by construction tools: saw, wrench, drill, hammer, level, paint roller and pliers"></div>

    <div class="phone">
      <svg viewBox="0 0 24 24" aria-hidden="true">
        <path d="M6.6 10.8a15.2 15.2 0 0 0 6.6 6.6l2.2-2.2a1 1 0 0 1 1-.25 11.4 11.4 0 0 0 3.6.57 1 1 0 0 1 1 1V20a1 1 0 0 1-1 1A17 17 0 0 1 3 4a1 1 0 0 1 1-1h3.5a1 1 0 0 1 1 1c0 1.25.2 2.45.57 3.6a1 1 0 0 1-.25 1z" fill="var(--yellow)"/>
      </svg>
      912-730-2591
    </div>

    <div class="web">
      <svg viewBox="0 0 24 24" aria-hidden="true" fill="none" stroke="var(--yellow)" stroke-width="1.6">
        <circle cx="12" cy="12" r="10"/>
        <ellipse cx="12" cy="12" rx="4.5" ry="10"/>
        <line x1="2" y1="12" x2="22" y2="12"/>
        <line x1="4" y1="7" x2="20" y2="7"/>
        <line x1="4" y1="17" x2="20" y2="17"/>
      </svg>
      BRINDLEWOODEQUIPMENT-EXAMPLE.COM
    </div>
  </div>
</body>
</html>
```